Wren Hollow Oils - Body Oils

I am in need of 4 different label and package designs for a new line of body oils that I am launching. I already have the logo and names, it is now a matter of positioning the content. The names are as follows;

1) CARDAMOM + CYPRESS
WARMING BODY OIL
2) NEROLI + LEMON
UPLIFTING BODY OIL
3) CEDAR + BIRCH
GROUNDING BODY OIL
4) SAGE + MINT
COOLING BODY OIL.
The size of each label is 13cm wide x 9.5cm high. The size of the box is 4.5cm x 4.5cm x 15.5cm high.
The size of the bottle is 4cm across the base and 10.5cm in glass height.
I have included an image from a line that I started to work on but it didn't go anywhere. I thought the borders looked good to frame it in however, I am not attached to anything at this point. I am also including a picture of a product line that has used different colors on the packaging. I am not certain that this is the direction I'd like to take however I like how it looks with them. If we were to add the color I think it should be JUST the boxes and NOT the labels and they would be as follows; WARMING OIL - warm burgundy, earth tones UPLIFTING OIL - warm light, lightish blues GROUNDING OIL - warm soft, brownish creams COOLING OIL - refreshing light, pale green possibly blue. I would be interested to see what adding a sprig of a plant would look like on the boxes however with the already busy logo it might look like too much is going on. As you will see in our instagram and website we currently have the bear logo in a foil. I am not sure that I want to proceed with this foil as it is difficult to photograph. I would like to look at colors that compliment the existing line of essential oils as well as the dark brown wood on the cap.
I have added a design that looks a bit industrial that I like, it reads black ops.

Target Market(s)

My market is mainly females who are interested in natural health age 17 - 70. There is a large movement for organic + green beauty. I would like the label to look and feel clean and natural. Something that has been wildcrafted, raw and completely from nature.

Industry/Entity Type

Health And Wellness

Colors

Designer to choose colors to be used in the design.

Requirements
Must have
• Appeal to very progressive organic consumers. Please see the pictures marked SAMPLES 1, 2, 3 + 4 for design ideas.
• Easy to read. Clean design.
• The following information should be on the label as well as the packaging box.
• Size - 100 ML
• Barcodes - still to come
• Ingredients:
• 1) CARDAMOM + CYPRESS WARMING BODY OIL - *Sunflower Oil, **Orange, **Cardamom, **Cypress, **Ginger *Organic, **Organic essential oil
• 2) NEROLI + LEMON UPLIFTING BODY OIL - *Sunflower oil, **Orange, **Neroli, **Grapefruit, **Lemon, **Bergamot, **Benzoin, *Organic, **Organic essential oil
• 3) CEDAR + BIRCH GROUNDING BODY OIL - *Sunflower Oil, **Cedarwood, **Birch, **Benzoin, **Patchouli,*Organic, **Organic essential oil
• 4) SAGE + MINT COOLING BODY OIL - *Sunflower oil, **Spearmint, **Clary Sage, **Geranium, **Ylang Ylang, *Organic, **Organic essential oil
• Suggested Use:
• Warm oil if desired. Apply to the full body after bathing, massage in motions toward the heart until the oil is mostly absorbed. Can also be added to bath water.
Nice to have
• I would like to see the designs on the actual bottle (pic included) to see how it looks.
Should not have
• Bright colors.

```html
<!DOCTYPE html>
<html lang="en">
<head>
<meta charset="utf-8">
<title>Wren Hollow Oils – Cardamom + Cypress Box Dieline</title>
<link rel="stylesheet" href="https://fonts.googleapis.com/css2?family=Oswald:wght@300;400;500&display=swap">
<style>
  :root {
    --page: #ffffff;
    --kraft: #b39f87;
    --kraft-edge: #a8937a;
    --fold: #5f5a55;
    --ink: #2b1d16;
    --band: #2e1a12;
    --cream: #d8c6a8;
  }
  html, body {
    margin: 0;
    padding: 0;
    width: 1103px;
    height: 1200px;
    overflow: hidden;
    background: var(--page);
  }
  .dieline { display: block; width: 1103px; height: 1200px; }
  .board { fill: var(--kraft); }
  .fold { stroke: var(--fold); stroke-width: 0.9; fill: none; }
  .rule { stroke: var(--ink); stroke-width: 1.6; }
  .brand-band { fill: var(--band); }
  .brand-name {
    font-family: "Oswald", sans-serif;
    font-weight: 400;
    fill: var(--cream);
    letter-spacing: 3px;
    font-size: 17px;
  }
  .title {
    font-family: "Oswald", sans-serif;
    font-weight: 500;
    fill: var(--ink);
    font-size: 17px;
    letter-spacing: 1.2px;
  }
  .subtitle {
    font-family: "Oswald", sans-serif;
    font-weight: 300;
    fill: var(--ink);
    font-size: 13px;
    letter-spacing: 1.4px;
  }
  .claim {
    font-family: "Oswald", sans-serif;
    font-weight: 300;
    fill: var(--ink);
    font-size: 12.5px;
    letter-spacing: 1.3px;
  }
  .volume {
    font-family: "Oswald", sans-serif;
    font-weight: 500;
    fill: var(--ink);
    font-size: 14px;
    letter-spacing: 1px;
  }
  .back-copy {
    font-family: "Oswald", sans-serif;
    font-weight: 300;
    fill: var(--ink);
    font-size: 10px;
    letter-spacing: 0.9px;
  }
</style>
</head>
<body>
<svg class="dieline" viewBox="0 0 1386 1508" preserveAspectRatio="none" xmlns="http://www.w3.org/2000/svg">

  <!-- board pieces -->
  <g class="board-pieces">
    <path class="board" d="M243 377 V125 Q243 97 271 97 H459 Q487 97 487 125 V377 Z"/>
    <path class="board" d="M463 367 V288 Q463 260 491 260 H708 V367 Z"/>
    <path class="board" d="M905 367 V260 H1120 Q1140 262 1148 320 V367 Z"/>
    <path class="board" d="M205 367 H1148 V1258 H463 V1148 H205 Q175 1148 175 1118 V397 Q175 367 205 367 Z"/>
    <path class="board" d="M683 1148 H928 V1392 Q928 1420 900 1420 H711 Q683 1420 683 1392 Z"/>
  </g>

  <!-- fold and crease lines -->
  <g class="folds">
    <line class="fold" x1="253" y1="377" x2="253" y2="1138"/>
    <line class="fold" x1="473" y1="280" x2="473" y2="1248"/>
    <line class="fold" x1="697" y1="377" x2="697" y2="1148"/>
    <line class="fold" x1="917" y1="280" x2="917" y2="1248"/>
    <line class="fold" x1="175" y1="377" x2="1148" y2="377"/>
    <line class="fold" x1="175" y1="1138" x2="1148" y2="1138"/>
    <line class="fold" x1="253" y1="158" x2="475" y2="158"/>
    <line class="fold" x1="697" y1="1360" x2="917" y2="1360"/>
    <path class="fold" d="M483 280 L483 357 M697 1148 Q690 1190 690 1248 M930 1148 Q935 1200 960 1248 H1140"/>
  </g>

  <!-- tuck flap band -->
  <rect class="brand-band" x="284" y="108" width="161" height="269"/>
  <g transform="rotate(180 365 250)">
    <text class="brand-name" x="365" y="244" text-anchor="middle">WREN HOLLOW</text>
    <text class="brand-name" x="365" y="266" text-anchor="middle">OILS</text>
  </g>

  <!-- front panel band -->
  <rect class="brand-band" x="724" y="377" width="161" height="286"/>
  <text class="brand-name" x="804" y="544" text-anchor="middle">WREN HOLLOW</text>
  <text class="brand-name" x="804" y="566" text-anchor="middle">OILS</text>

  <!-- front panel copy -->
  <g class="front-copy">
    <text class="title" x="715" y="709">CARDAMOM + CYPRESS</text>
    <line class="rule" x1="715" y1="719" x2="893" y2="719"/>
    <text class="title" x="715" y="744">WARMING BODY OIL</text>
    <line class="rule" x1="715" y1="753" x2="893" y2="753"/>
    <text class="subtitle" x="715" y="773">ORGANIC BOTANICALS</text>
    <line class="rule" x1="715" y1="783" x2="893" y2="783"/>
    <text class="claim" x="715" y="802">REVITALIZING AND</text>
    <text class="claim" x="715" y="820">STIMULATING FOR A</text>
    <text class="claim" x="715" y="838">RENEWED SENSE OF</text>
    <text class="claim" x="715" y="856">SPIRIT</text>
    <line class="rule" x1="852" y1="790" x2="852" y2="858"/>
    <text class="volume" transform="translate(881 824) rotate(-90)" text-anchor="middle">100ML</text>
    <line class="rule" x1="715" y1="866" x2="893" y2="866"/>
  </g>

  <!-- back panel copy -->
  <g class="back-panel">
    <text class="back-copy" x="364" y="635" text-anchor="middle">SUGGESTED USE</text>
    <text class="back-copy" x="276" y="664" textLength="176" lengthAdjust="spacing">WARM OIL IF DESIRED. APPLY TO THE</text>
    <text class="back-copy" x="276" y="678" textLength="176" lengthAdjust="spacing">FULL BODY AFTER BATHING, MASSAGE</text>
    <text class="back-copy" x="276" y="693" textLength="176" lengthAdjust="spacing">IN MOTIONS TOWARD THE HEART</text>
    <text class="back-copy" x="276" y="707" textLength="176" lengthAdjust="spacing">UNTIL THE OIL IS MOSTLY ABSORBED.</text>
    <text class="back-copy" x="276" y="722" textLength="176" lengthAdjust="spacing">CAN ALSO BE ADDED TO BATH WATER.</text>
    <line class="rule" x1="275" y1="749" x2="452" y2="749" style="stroke-width:1"/>
    <text class="back-copy" x="276" y="780" textLength="178" lengthAdjust="spacing">*SUNFLOWER OIL, **ORANGE,</text>
    <text class="back-copy" x="276" y="794" textLength="178" lengthAdjust="spacing">**CARDAMOM, **CYPRESS, **GINGER</text>
    <text class="back-copy" x="365" y="809" text-anchor="middle">*ORGANIC,</text>
    <line class="rule" x1="275" y1="837" x2="452" y2="837" style="stroke-width:1"/>
    <text class="back-copy" x="365" y="867" text-anchor="middle">WWW.WRENHOLLOWOILS.COM</text>
  </g>
</svg>
</body>
</html>
```